Bluefinch Painting needs a Website

We need a website built for a Painting company I own, we mainly do residential painting, but don't want to be limited to that.

Need to have estimate request form.
Need pic's of past projects

I like the look of the website for http://www.harborline-painters.example
& "Thistledown Property inspections"

My logo that was designed here on ArtHive on the front page

I would like one of the houses I downloaded as part of the background
of the front page.

Target Market(s)

Home owners

Industry/Entity Type

Painting

Number of Pages Required

1 page

Font styles to use
Serif

Requirements
Must have
• Estimate request form for home owners to fill out -
• Name:
• Phone Number:
• Address:
• E-mail:
• Painting project description:
• And my info to:
• My phone number: (555) 318-7764
• My web address bluefinchpainting.example
Nice to have
• My logo that was designed here on ArtHive

```html
<!DOCTYPE html>
<html lang="en">
<head>
<meta charset="utf-8">
<title>Bluefinch Painting</title>
<link href="https://fonts.googleapis.com/css2?family=Noto+Serif:ital,wght@0,400;0,700;1,400&family=Open+Sans:wght@400;600&display=swap" rel="stylesheet">
<style>
:root{
  --blue:#1c86d1;
  --blue-dark:#1468aa;
  --blue-light:#3db2ec;
  --blue-pale:#8fd6f7;
  --ink:#333a40;
  --muted:#6b7278;
  --paper:#f4f4f2;
  --white:#ffffff;
  --footer:#141a22;
  --footer-text:#b9c2cc;
  --serif:"Noto Serif", Georgia, serif;
  --sans:"Open Sans", Arial, sans-serif;
}
*{box-sizing:border-box;margin:0;padding:0}
html,body{width:1200px;height:2532px;overflow:hidden}
body{background:var(--paper);font-family:var(--serif);color:var(--ink);position:relative}

/* header */
.site-header{height:101px;background:var(--blue);position:relative}
.social{position:absolute;left:50px;top:36px;display:flex;gap:10px}
.social span{width:26px;height:26px;border-radius:50%;border:2px solid rgba(255,255,255,.85)}
.brand{position:absolute;left:50%;top:22px;transform:translateX(-50%);display:flex;align-items:center;gap:14px}
.brand-mark{width:52px;height:52px;background:var(--white)}
.brand-name{font-family:var(--serif);font-size:34px;line-height:1;color:var(--white);letter-spacing:2px;white-space:nowrap}
.help{position:absolute;right:50px;top:22px;color:var(--white)}
.help small{display:block;font-family:var(--sans);font-size:15px;opacity:.85}
.help strong{font-family:var(--sans);font-size:30px;font-weight:600}

/* nav */
.main-nav{height:51px;background:var(--white);display:flex;padding-left:50px;box-shadow:0 2px 4px rgba(0,0,0,.08);position:relative;z-index:1}
.main-nav a{font-family:var(--sans);font-size:18px;color:#333;text-decoration:none;text-transform:uppercase;display:flex;align-items:center;justify-content:center;width:172px}
.main-nav a.active{background:var(--blue-light);color:var(--white)}

/* hero */
.hero{height:564px;background:linear-gradient(180deg,#7fa9d2 0%,#aac4dc 12%,#5d6166 24%,#9a8f7c 36%,#b5a78e 46%,#6f7f52 56%,#3f5a33 64%,#e9ebec 72%,#c9cbcc 78%,#55585b 88%,#77797a 100%)}

/* welcome */
.welcome{position:relative;height:595px}
.welcome h1{position:absolute;left:50px;top:30px;font-size:27px;font-weight:400;color:var(--ink)}
.welcome h1 em{font-style:normal;color:var(--blue)}
.rule{display:block;width:90px;height:3px;background:var(--blue);margin-top:14px}
.welcome .intro{position:absolute;left:50px;top:92px;width:700px;font-size:15px;line-height:1.75;color:var(--muted)}
.services{position:absolute;left:51px;top:234px;width:702px;display:grid;grid-template-columns:repeat(4,175px);grid-template-rows:150px 152px;gap:4px 0}
.svc-photo{background:linear-gradient(160deg,#f2efe9 0%,#c9b79a 45%,#8a3a2e 75%,#4a3a2e 100%)}
.svc-photo.dark{background:linear-gradient(160deg,#1d2631 0%,#3a4a58 45%,#6b5a48 75%,#2a3440 100%)}
.svc-photo.house{background:linear-gradient(180deg,#dfe8ef 0%,#b8a68a 40%,#8c7c66 60%,#4f6d3a 85%,#3c5a2d 100%)}
.svc-photo.light{background:linear-gradient(160deg,#f4f7f9 0%,#d8e2e8 50%,#8ea0ae 100%)}
.svc-text{background:var(--white);padding:14px 12px}
.svc-text h3{font-size:17px;line-height:1.15;color:var(--blue);text-transform:uppercase;margin-bottom:10px}
.svc-text p{font-size:14px;line-height:1.45;color:var(--muted)}

/* roller-shaped quote panel */
.quote-panel{position:absolute;left:782px;top:44px;width:395px;height:505px}
.quote-head{position:absolute;left:0;right:0;top:0;height:86px;border-radius:14px;background:linear-gradient(180deg,var(--blue-pale) 0%,var(--blue-light) 35%,#2a9ddd 80%,var(--blue) 100%);box-shadow:0 3px 6px rgba(0,0,0,.18);color:var(--white);font-size:38px;letter-spacing:2px;display:flex;align-items:center;justify-content:center;z-index:2}
.quote-head:before,.quote-head:after{content:"";position:absolute;top:12px;bottom:12px;width:8px;background:var(--blue-dark);border-radius:4px}
.quote-head:before{left:-6px}
.quote-head:after{right:-6px}
.quote-body{position:absolute;top:78px;left:0;right:0;bottom:0;background:linear-gradient(180deg,var(--blue) 0%,#2391da 100%);padding:38px 28px 0}
.field{width:100%;height:40px;background:var(--white);margin-bottom:11px;padding:0 12px;font-family:var(--serif);font-style:italic;font-size:14px;color:#9aa3aa;display:flex;align-items:center}
.field.area{height:92px;align-items:flex-start;padding-top:10px}
.submit{display:block;text-align:center;color:var(--white);font-size:22px;font-weight:700;letter-spacing:1px;margin-top:40px}
.quote-edge{position:absolute;left:0;bottom:-1px;width:395px;height:22px}

/* testimonials */
.clients{height:289px;background:var(--blue);position:relative;color:var(--white)}
.client-photo{position:absolute;left:63px;top:30px;width:228px;height:228px;border-radius:50%;border:6px solid #e9eef2;background:linear-gradient(180deg,#e8e8e6 0%,#d9b08c 40%,#b9785a 65%,#c8362e 100%)}
.clients h2{position:absolute;left:324px;top:30px;font-size:25px;font-weight:400;text-transform:uppercase}
.clients h2 .rule{background:var(--white);width:70px;margin-top:10px}
.clients blockquote{position:absolute;left:324px;top:92px;width:825px;font-style:italic;font-size:17px;line-height:1.6}
.clients cite{position:absolute;left:324px;top:196px;font-style:normal;font-size:20px}
.dots{position:absolute;left:324px;top:240px;display:flex;gap:8px}
.dots span{width:16px;height:3px;background:rgba(255,255,255,.55)}
.dots span:first-child{background:var(--white)}

/* projects */
.projects{height:572px;position:relative}
.projects h2{position:absolute;left:50px;top:30px;font-size:27px;font-weight:400;text-transform:uppercase}
.projects h2 em{font-style:normal;color:var(--blue)}
.projects .rule{width:80px}
.projects .intro{position:absolute;left:50px;top:86px;width:1100px;font-size:14px;line-height:1.6;color:var(--muted)}
.tabs{position:absolute;left:50px;top:150px;display:flex;font-size:18px;color:#555}
.tabs span+span:before{content:"/";margin:0 22px;color:#888}
.tabs .on{color:var(--blue)}
.gallery{position:absolute;left:51px;top:198px;width:1094px;display:grid;grid-template-columns:repeat(5,1fr);grid-template-rows:168px 168px}
.gallery .featured{background:linear-gradient(180deg,#2b2f33,#3a3f44);display:flex;flex-direction:column;align-items:center;justify-content:center;color:var(--white);font-size:16px;gap:14px}
.g-dining{background:linear-gradient(180deg,#e8c8b8 0%,#c98a78 35%,#f1e4d4 55%,#a4432f 80%,#6e2a22 100%)}
.g-office{background:linear-gradient(180deg,#f7f7f5 0%,#e4e1da 40%,#6e9a4a 62%,#d9d5cc 80%,#b2aca0 100%)}
.g-hall{background:linear-gradient(180deg,#6a4a2e 0%,#e3b470 30%,#c0733a 55%,#7a3f25 80%,#4b2a1a 100%)}
.g-restaurant{background:linear-gradient(180deg,#f0d7a0 0%,#e1b873 35%,#b85a3a 65%,#e9dcc4 85%,#9a6a4a 100%)}
.g-bath{background:linear-gradient(180deg,#ffffff 0%,#e9eef1 40%,#bcd2dd 60%,#f4f4f2 80%,#c9ccce 100%)}
.g-living{background:linear-gradient(180deg,#e2d4c0 0%,#c9a783 40%,#f3ece2 65%,#8c6a4e 100%)}
.g-corridor{background:linear-gradient(180deg,#f1e8e0 0%,#caa29a 35%,#7c6a8a 60%,#e7e3e9 80%,#a49ab0 100%)}
.g-lounge{background:linear-gradient(180deg,#3a2c24 0%,#9a4a2e 35%,#d9b088 60%,#f0e6d8 80%,#8c7a66 100%)}
.g-hallway{background:linear-gradient(180deg,#3c3a36 0%,#9a8e78 40%,#e8dfc8 65%,#6a5a48 100%)}

/* footer */
.site-footer{height:360px;background:var(--footer);position:relative;color:var(--footer-text)}
.site-footer h2{position:absolute;left:50px;top:38px;font-size:23px;font-weight:400;color:var(--blue-light);text-transform:uppercase}
.contact{position:absolute;left:50px;top:100px;list-style:none;font-size:16px;line-height:1.45}
.contact li{display:flex;gap:14px;margin-bottom:30px}
.contact svg{flex:none;margin-top:3px}
.map{position:absolute;left:598px;top:43px;width:545px;height:186px;border:4px solid var(--blue-light);background:linear-gradient(135deg,#ece6d4 0%,#e3dcc4 50%,#cfdcc4 100%)}
.footer-bar{position:absolute;left:0;right:0;bottom:0;height:64px;border-top:1px solid #2a323c;display:flex;align-items:center;justify-content:space-between;padding:0 50px;font-family:var(--sans);font-size:13px}
.footer-bar nav a{color:var(--footer-text);text-decoration:none}
.footer-bar nav a:first-child{color:var(--white)}
.footer-bar nav a+a:before{content:"/";margin:0 10px;color:#6d7782}
</style>
</head>
<body>

<header class="site-header">
  <div class="social"><span></span><span></span><span></span><span></span><span></span></div>
  <div class="brand"><span class="brand-mark"></span><span class="brand-name">BLUEFINCH PAINTING</span></div>
  <div class="help"><small>Need help?</small><strong>555.318.7764</strong></div>
</header>

<nav class="main-nav">
  <a class="active" href="#">Home</a><a href="#">About Us</a><a href="#">Services</a><a href="#">Projects</a><a href="#">Free Quote</a><a href="#">Contact Us</a>
</nav>

<section class="hero" role="img" aria-label="Photo of a two-storey house with a company pickup truck and trailer parked in the driveway"></section>

<section class="welcome">
  <h1>WELCOME TO <em>BLUEFINCH PAINTING</em><span class="rule"></span></h1>
  <p class="intro">Lorem ipsum dolor sit amet, consectetur adipiscing elit. Donec lacinia nulla enim, sit amet dignissim turpis rhoncus non. Integer est erat, egestas in mauris vitae, feugiat sollicitudin nulla. Duis sit amet lorem eget mauris aliquam gravida eu quis ligula. Cum sociis natoque penatibus et magnis dis parturient montes, nascetur ridiculus mus. Donec nec tempor tellus, eu feugiat urna. Curabitur vel sodales tellus.</p>

  <div class="services">
    <div class="svc-photo dark" role="img" aria-label="Photo of a house exterior at dusk"></div>
    <div class="svc-text"><h3>Exterior Painting</h3><p>Lorem ipsum dolor sit amet, consectet ur adipiscing elit.</p></div>
    <div class="svc-photo" role="img" aria-label="Photo of a painted kitchen interior"></div>
    <div class="svc-text"><h3>Interior Painting</h3><p>Lorem ipsum dolor sit amet, consectet ur adipiscing elit.</p></div>
    <div class="svc-text"><h3>Residential Painting</h3><p>Lorem ipsum dolor sit amet, consectet ur adipiscing elit.</p></div>
    <div class="svc-photo house" role="img" aria-label="Photo of a residential house with garden"></div>
    <div class="svc-text"><h3>Commercial Painting</h3><p>Lorem ipsum dolor sit amet, consectet ur adipiscing elit.</p></div>
    <div class="svc-photo light" role="img" aria-label="Photo of a bright office interior"></div>
  </div>

  <form class="quote-panel">
    <div class="quote-body">
      <span class="field">Name:</span>
      <span class="field">E-mail:</span>
      <span class="field">Phone Number:</span>
      <span class="field">Address:</span>
      <span class="field area">Painting project description:</span>
      <span class="submit">SUBMIT</span>
      <svg class="quote-edge" viewBox="0 0 395 22" preserveAspectRatio="none" aria-hidden="true"><path d="M0 10 Q20 2 40 12 T80 10 T120 14 T160 8 T200 13 T240 9 T280 14 T320 8 T360 12 T395 9 V22 H0 Z" fill="#f4f4f2"/></svg>
    </div>
    <div class="quote-head">FREE QUOTE</div>
  </form>
</section>

<section class="clients">
  <div class="client-photo" role="img" aria-label="Portrait photo of a client"></div>
  <h2>Our Clients Say<span class="rule"></span></h2>
  <blockquote>“ Lorem ipsum dolor sit amet, consectetur adipiscing elit. Sed turpis sapien, lobortis vitae nisl at, mattis v pretium purus. Nullam ultrices sapien neque, nec venenatis nisl feugiat eu. Nulla rutrum eros enim, quis iaculis ligula euismod nec lorem !”</blockquote>
  <cite>Lorem ipsum</cite>
  <div class="dots"><span></span><span></span><span></span><span></span></div>
</section>

<section class="projects">
  <h2>Features <em>Projects</em><span class="rule"></span></h2>
  <p class="intro">Lorem Ipsum is simply dummy text of the printing and typesetting industry. Lorem Ipsum has been the industry's standard dummy text ever since the 1500s, when an unknown printer took a galley.....</p>
  <div class="tabs"><span class="on">Exterior</span><span>Interior</span><span>Residential</span><span>Commercial</span></div>
  <div class="gallery">
    <div class="featured" role="img" aria-label="Project photo">
      Lorem Ipsum is simply
      <svg width="34" height="34" viewBox="0 0 34 34" aria-hidden="true"><circle cx="14" cy="14" r="10" fill="none" stroke="#fff" stroke-width="3"/><path d="M21 21l9 9M14 9v10M9 14h10" stroke="#fff" stroke-width="3"/></svg>
    </div>
    <div class="g-dining" role="img" aria-label="Project photo of a restaurant dining room"></div>
    <div class="g-office" role="img" aria-label="Project photo of an office with plants"></div>
    <div class="g-hall" role="img" aria-label="Project photo of a dining hall"></div>
    <div class="g-restaurant" role="img" aria-label="Project photo of a restaurant interior"></div>
    <div class="g-bath" role="img" aria-label="Project photo of a white bathroom"></div>
    <div class="g-living" role="img" aria-label="Project photo of a living room"></div>
    <div class="g-corridor" role="img" aria-label="Project photo of an office corridor"></div>
    <div class="g-lounge" role="img" aria-label="Project photo of a lounge"></div>
    <div class="g-hallway" role="img" aria-label="Project photo of a hallway"></div>
  </div>
</section>

<footer class="site-footer">
  <h2>Get in Tuch</h2>
  <ul class="contact">
    <li><svg width="16" height="20" viewBox="0 0 16 20" aria-hidden="true"><path d="M8 0a7 7 0 0 0-7 7c0 5 7 13 7 13s7-8 7-13a7 7 0 0 0-7-7z" fill="#3db2ec"/><circle cx="8" cy="7" r="2.5" fill="#141a22"/></svg><span>Bluefinch Painting<br>123 Lorem ipsum Dolor, Site Amet, USA, 12345</span></li>
    <li><svg width="16" height="18" viewBox="0 0 16 18" aria-hidden="true"><path d="M3 1l3 0 1 4-2 1.5c1 2.5 2.5 4 5 5L11.5 9l4 1v3c0 1-1 2-2 2C7 15 1 9 1 3c0-1 1-2 2-2z" fill="#3db2ec"/></svg><span>555.318.7764</span></li>
    <li><svg width="18" height="14" viewBox="0 0 18 14" aria-hidden="true"><rect x="0.5" y="0.5" width="17" height="13" fill="#3db2ec"/><path d="M1 1l8 7 8-7" fill="none" stroke="#141a22" stroke-width="1.5"/></svg><span>info@bluefinchpainting.example</span></li>
  </ul>
  <div class="map" role="img" aria-label="Road map of the service area"></div>
  <div class="footer-bar">
    <nav><a href="#">Home</a><a href="#">About Us</a><a href="#">Services</a><a href="#">Projects</a><a href="#">Free Quote</a><a href="#">Contact Us</a></nav>
    <span>Copyright © 2015. Bluefinch Painting . All Right Reserved.</span>
  </div>
</footer>

</body>
</html>
```